Tessaro Lane Website

We are starting a marketing company and to do that we need a website! We want a website that will inspire and persuade to bring out the awesomeness in our clients.
What we want to see:
- Inspirational and persuasive imagery that relate to Branding.
- No cliche images eg. business man, suits and hand shakes
- We want to transform and educate our clients.
- We want to show them the path and would like our website to really act as a guide that guides them step by step through our process.
- We want the portray that we are an investment but not have a pretentious way to it. We put our heart into every project and that is how we treat our clients.
-When you submit your design please include what platform you have created for. Preference would be Wordpress or Joobla.

We have included the psd file for the wire frame, logo files, font files, site map and a link to a video we create to give you more information on what we would like to see. http://clipvault-demo.example/t/qx903LmaP

Feel free to make small modification to the logos if you think it will improve it. Your creativity and advice is most welcome.

One thing we forgot. We would like to have our contact information near the top of the website as well as at the bottom.  Here is out contact info:

Email: info@tessarolane.ca
Phone: 555-013-4829

Reason: As we are new with the platform and that we want to optimize our results, we decided to extend the deadline by 15 days. Thanks!

Target Market(s)

28-60, Male and Female, Oil field, Local Businesses, Dentists, Chiropractors, Hair salon, Construction/Renovation, Events etc

Industry/Entity Type

Investment

Requirements
Must have
• - 4 Inspirational and persuasive Imagery for the top portion of the website
- Must have a feel as if your not on a website an example of this is linked below.
http://www.pitchgallery-demo.example/design/482907/web-design-by-dalia-fenwick
Nice to have
• - Creative advice from you.
- Creative buttons for Get Free Quote and Subscribe buttons. Something out of the box that draws peoples attention. eg. a 'B' button. Just and example but still something related to branding.
Should not have
• No Cliches

```html
<!DOCTYPE html>
<html lang="en">
<head>
<meta charset="utf-8">
<title>Tessaro Lane</title>
<link rel="stylesheet" href="https://fonts.googleapis.com/css2?family=Figtree:wght@400;600;700;800&display=swap">
<style>
:root{
  --green:#84b135;
  --green-dark:#4d7f2a;
  --green-pale:#e4eed4;
  --slate:#1c2a33;
  --slate-text:#5b6a72;
  --grey:#7a7b7d;
  --grey-text:#6a6a6a;
  --body-text:#9a9a9a;
  --white:#ffffff;
  --nav-bg:rgba(242,244,245,.92);
}
*{box-sizing:border-box;margin:0;padding:0}
html,body{width:1200px;height:866px;overflow:hidden;background:var(--white)}
body{position:relative;font-family:"Figtree",Arial,sans-serif}
.abs{position:absolute}
.hero{left:0;top:0;width:1200px;height:515px;
  background:linear-gradient(180deg,#d9f1f7 0%,#a9cedd 35%,#6f9cb5 70%,#3f6f90 100%)}
.brand{left:130px;top:62px}
.brand-name{display:flex;align-items:center;gap:10px;font-size:36px;font-weight:800;color:var(--grey-text);line-height:1}
.brand-dot{width:22px;height:22px;border-radius:50%;background:var(--green)}
.main-nav{left:130px;top:207px;list-style:none}
.main-nav li{display:block;margin-bottom:5px}
.main-nav a{display:inline-block;height:27px;line-height:28px;padding:0 10px;font-size:22px;color:var(--grey-text);background:var(--nav-bg);text-decoration:none;letter-spacing:.3px}
.main-nav a.is-active{background:var(--green);color:var(--white)}
.top-contact{left:850px;top:362px;color:var(--white);font-size:19px}
.top-contact div{display:flex;align-items:center;gap:10px;height:31px}
.top-contact svg{width:27px}
.steps{left:130px;top:447px;display:flex;gap:20px}
.step{position:relative;width:220px;height:48px;background:var(--slate);color:var(--slate-text);font-size:20px;font-weight:700;display:flex;align-items:center;justify-content:center}
.step.is-current{background:var(--green);color:var(--white)}
.step.is-current::before{content:"";position:absolute;left:102px;top:-9px;border:9px solid transparent;border-top:0;border-bottom-color:var(--green)}
.band{left:0;top:515px;width:1200px;height:53px;background:var(--green)}
.social{left:130px;top:530px;display:flex;gap:4px}
.social span{width:25px;height:25px;border-radius:50%;background:var(--green-pale)}
.newsletter{left:292px;top:525px;width:778px;height:54px;background:var(--grey);border:2px solid var(--white);color:var(--white);font-weight:700}
.newsletter h3{position:absolute;left:20px;top:12px;font-size:23px;font-weight:700;line-height:26px}
.newsletter p{position:absolute;left:216px;top:17px;font-size:16px;letter-spacing:.3px;line-height:20px}
.newsletter .email{position:absolute;left:443px;top:13px;width:204px;height:28px;background:var(--white);color:#aaa;font-weight:400;font-size:15px;padding:4px 10px}
.newsletter .subscribe{position:absolute;left:659px;top:12px;width:100px;height:30px;background:var(--green);border:2px solid var(--white);font-size:16px;display:flex;align-items:center;justify-content:center}
.welcome{left:130px;top:608px;font-size:36px;font-weight:800;color:var(--green-dark)}
.intro{left:307px;top:611px;width:764px;font-family:Arial,Helvetica,sans-serif;font-size:12px;letter-spacing:.12px;line-height:14.5px;color:var(--body-text)}
.quote-btn{left:308px;top:700px;width:244px;height:41px;background:var(--grey);color:var(--white);font-size:26px;font-weight:700;display:flex;align-items:center;justify-content:center}
.base{left:0;top:808px;width:1200px;height:58px;background:var(--grey)}
.footer{left:130px;top:779px;width:940px;height:61px;background:var(--green);border:2px solid var(--white)}
.footer-brand{left:20px;top:20px;color:var(--white)}
.footer-brand .brand-name{font-size:16px;color:var(--white);gap:5px}
.footer-brand .brand-dot{width:10px;height:10px;background:var(--white)}
.footer-links{left:175px;top:14px;display:flex;font-family:Arial,sans-serif;font-size:12px;color:var(--white)}
.footer-links span{padding:0 19px;border-left:1px solid var(--white);line-height:13px}
.footer-links span:first-child{padding-left:0;border:0}
.legal{left:175px;top:33px;font-family:Arial,sans-serif;font-size:12px;color:#cfe3ad}
.footer-contact{left:764px;top:10px;font-family:Arial,sans-serif;font-size:12px;color:var(--white)}
.footer-contact div{display:flex;align-items:center;gap:12px;height:19px}
.footer-contact svg{width:19px}
</style>
</head>
<body>
<div class="abs hero" role="img" aria-label="Photograph of a long suspension footbridge disappearing into blue morning fog over water"></div>

<div class="abs brand">
  <div class="brand-name"><span class="brand-dot"></span>Tessaro Lane</div>
</div>

<ul class="abs main-nav">
  <li><a class="is-active" href="#">STRATEGY</a></li>
  <li><a href="#">PORTFOLIO</a></li>
  <li><a href="#">ABOUT US</a></li>
  <li><a href="#">CONTACT US</a></li>
  <li><a href="#">BLOG</a></li>
</ul>

<div class="abs top-contact">
  <div><svg viewBox="0 0 27 18"><rect width="27" height="18" rx="2" fill="#fff"/><path d="M1 2l12.5 9L26 2" fill="none" stroke="#8fb3c7" stroke-width="1.5"/></svg>info@tessarolane.ca</div>
  <div><svg viewBox="0 0 27 24"><path d="M6 1l4 5-2 3c1 3 4 6 7 8l3-2 5 4-3 4C10 23 2 13 3 4z" fill="#fff"/></svg>555-013-4829</div>
</div>

<div class="abs steps">
  <div class="step is-current">Tessaro Lane</div>
  <div class="step">Be Found</div>
  <div class="step">Connect</div>
  <div class="step">Get Growing</div>
</div>

<div class="abs band"></div>
<div class="abs social"><span></span><span></span><span></span><span></span></div>

<div class="abs newsletter">
  <h3>Get Tips &amp; Tricks!</h3>
  <p>Subscribe to our Newsletter</p>
  <div class="email">email address ...</div>
  <div class="subscribe">Subscribe</div>
</div>

<h1 class="abs welcome">Welcome</h1>
<p class="abs intro">Praesent sollicitudin malesuada interdum. Quisque enim dui, dictum quis ullamcorper et, volutpat non libero. Ut nibh nunc, mollis ac luctus eu, consectetur sodales tellus. In hac habitasse platea dictumst. Proin rutrum, mi vel condimentum egestas, mauris nulla malesuada est, a placerat velit felis a metus. Duis nec tellus lorem. Fusce elit ante, ullamcorper eu facilisis a, dapibus a neque. Lorem ipsum dolor sit amet, consectetur adipiscing elit. Donec ut orci quis quam aliquet pellentesque eu scelerisque lacus. Suspendisse potenti. Sed malesuada sem sit amet tellus facilisis ut iaculis eros gravida. Ut eu magna et velit mattis varius. Suspendisse potenti.</p>
<div class="abs quote-btn">Get a Free Quote</div>

<div class="abs base"></div>
<footer class="abs footer">
  <div class="abs footer-brand">
    <div class="brand-name"><span class="brand-dot"></span>Tessaro Lane</div>
  </div>
  <nav class="abs footer-links"><span>Sitemap</span><span>Strategy</span><span>Portfolio</span><span>About Us</span><span>Contact Us</span><span>Blog</span></nav>
  <div class="abs legal">© Tessaro Lane Inc. 2013 &nbsp;&nbsp; Privacy Policy &nbsp;|&nbsp; Terms &amp; Conditions</div>
  <div class="abs footer-contact">
    <div><svg viewBox="0 0 19 13"><rect width="19" height="13" rx="1" fill="#e4eed4"/><path d="M1 1.5l8.5 6 8.5-6" fill="none" stroke="#84b135" stroke-width="1.2"/></svg>info@tessarolane.ca</div>
    <div><svg viewBox="0 0 19 17"><path d="M4 1l3 3.5-1.5 2c.8 2 3 4.2 5 5.5l2-1.5 3.5 3-2 2.5C7 16 1 9 2 2.5z" fill="#e4eed4"/></svg>555-013-4829</div>
  </div>
</footer>
</body>
</html>
```